Building Company Business Card Design

I am looking to get a business card designed for my Building Company. Please find the logo attached.

Industry/Entity Type

Business

Contact Information for Business Card

Mobile 0472 913 046
Email admin@tarrowconstructworks.com.au
Website www.tarrowconstructworks.com.au

Colors
0255a3

```html
<!DOCTYPE html>
<html lang="en">
<head>
<meta charset="utf-8">
<title>Tarrow Constructworks – Business Card</title>
<link href="https://fonts.googleapis.com/css2?family=Lato:wght@400;700&family=Montserrat:wght@600&display=swap" rel="stylesheet">
<style>
  :root {
    --brand-blue: #0255a3;
    --ink: #222;
    --grey: #6a6a6a;
    --card-dark: #282828;
    --card-light: #fbfbfb;
    --backdrop: #e4e4e4;
  }
  * { box-sizing: border-box; margin: 0; padding: 0; }
  html, body { width: 1200px; height: 1200px; overflow: hidden; }
  body {
    background: var(--backdrop);
    font-family: "Lato", sans-serif;
    position: relative;
  }
  .card {
    position: absolute;
    left: 219px;
    width: 762px;
    height: 434px;
    box-shadow: 0 6px 18px rgba(0,0,0,0.25);
  }
  .card--front { top: 90px; background: var(--card-dark); }
  .card--back { top: 640px; background: var(--card-light); }

  .brand {
    position: absolute;
    display: flex;
    align-items: center;
    gap: 10px;
    font-family: "Montserrat", sans-serif;
    font-weight: 600;
    color: var(--brand-blue);
    letter-spacing: 0.04em;
    white-space: nowrap;
  }
  .brand__dot {
    width: 14px; height: 14px; border-radius: 50%;
    background: var(--brand-blue);
  }
  .card--front .brand {
    top: 170px; left: 0; right: 0; justify-content: center;
    font-size: 30px;
  }
  .card--back .brand {
    top: 60px; right: 26px;
    font-size: 26px;
  }
  .front-url {
    position: absolute; top: 320px; left: 0; right: 0;
    text-align: center; font-size: 17px; color: var(--grey);
  }
  .front-url span { color: var(--brand-blue); }

  .person { position: absolute; left: 49px; top: 155px; }
  .person__name {
    font-family: "Montserrat", sans-serif; font-weight: 600;
    font-size: 29px; color: var(--brand-blue); letter-spacing: 0.01em;
  }
  .person__role { font-size: 22px; font-weight: 700; color: var(--grey); margin-top: 4px; }

  .contacts { position: absolute; left: 49px; top: 296px; list-style: none; }
  .contacts li {
    display: flex; align-items: center; gap: 8px;
    font-size: 18px; color: var(--ink); height: 29px;
  }
  .contacts svg { width: 17px; height: 17px; fill: var(--brand-blue); flex: none; }

  .address {
    position: absolute; left: 494px; top: 332px;
    font-size: 18px; line-height: 23px; color: var(--ink);
  }
</style>
</head>
<body>
  <section class="card card--front">
    <div class="brand"><span class="brand__dot"></span>TARROW CONSTRUCTWORKS</div>
    <p class="front-url">www.<span>tarrowconstructworks</span>.com.au</p>
  </section>

  <section class="card card--back">
    <div class="brand"><span class="brand__dot"></span>TARROW CONSTRUCTWORKS</div>

    <div class="person">
      <h1 class="person__name">CALLUM REYES</h1>
      <p class="person__role">Director</p>
    </div>

    <ul class="contacts">
      <li>
        <svg viewBox="0 0 16 16" aria-hidden="true"><path d="M4 0h8a1.5 1.5 0 0 1 1.5 1.5v13A1.5 1.5 0 0 1 12 16H4a1.5 1.5 0 0 1-1.5-1.5v-13A1.5 1.5 0 0 1 4 0zm0 2v10.5h8V2zm4 11.3a.9.9 0 1 0 0 1.8.9.9 0 0 0 0-1.8z"/></svg>
        0472 913 046
      </li>
      <li>
        <svg viewBox="0 0 16 16" aria-hidden="true"><path d="M0 3h16v10H0zm1.6 1.2L8 9l6.4-4.8zM1.2 5.4v6.4l4.2-3.2zm13.6 0-4.2 3.2 4.2 3.2zM6.4 9.3l-4.8 3.5h12.8L9.6 9.3 8 10.5z"/></svg>
        admin@tarrowconstructworks.com.au
      </li>
      <li>
        <svg viewBox="0 0 16 16" aria-hidden="true"><path d="M8 0a8 8 0 1 0 0 16A8 8 0 0 0 8 0zm5.9 7.3h-2.6a12 12 0 0 0-.8-4.8 6.6 6.6 0 0 1 3.4 4.8zM8 1.5c.8.9 1.7 2.9 1.9 5.8H6.1C6.3 4.4 7.2 2.4 8 1.5zM5.5 2.5a12 12 0 0 0-.8 4.8H2.1a6.6 6.6 0 0 1 3.4-4.8zM2.1 8.7h2.6a12 12 0 0 0 .8 4.8 6.6 6.6 0 0 1-3.4-4.8zM8 14.5c-.8-.9-1.7-2.9-1.9-5.8h3.8c-.2 2.9-1.1 4.9-1.9 5.8zm2.5-1a12 12 0 0 0 .8-4.8h2.6a6.6 6.6 0 0 1-3.4 4.8z"/></svg>
        www.tarrowconstructworks.com.au
      </li>
    </ul>

    <p class="address">PO Box 3187 HARLOW<br>MAIL CENTRE, QLD 4812</p>
  </section>
</body>
</html>
```